Website Design - clean, cutting-edge, impressive and lively

We need to upgrade the design (content will stay the same) of our current site: https://brightpane.example/index.php?lang=en
1. We need a design that is more sophisticated, cutting-edge, and impressive.
2. At the same time, it is important for the site to remain clean and clear (to create feeling of transparency and trust with client).
3. Lastly, the site design must be in line with our logo in its projection of a service that is friendly and sites that are lively.
Target Market(s)
medium-sized businesses, such as VCs, Pharma, and other companies that need brochure-like sites (not ecommerce and not sites dependent on active online marketing).
Industry/Entity Type
Website
Number of Pages Required
2 page
Look and feel
Each slider illustrates characteristics of the customer's brand and the style your logo design should communicate.

```html
<!DOCTYPE html>
<html lang="en">
<head>
<meta charset="utf-8">
<title>BrightPane — We Create The Web</title>
<link rel="stylesheet" href="https://fonts.googleapis.com/css2?family=Poppins:wght@300;400;500;600;700;800;900&display=swap">
<style>
:root{
  --orange:#f15a24;
  --orange-deep:#ef5b25;
  --purple:#6a4aa5;
  --purple-tab:#6d4ca8;
  --yellow:#f7b500;
  --green:#8cc63f;
  --green-tab:#8dc63f;
  --ink:#2b2b2b;
  --muted:#777;
  --faint:#efefef;
  --footer:#3b3b3b;
  --footer-base:#2e2e2e;
  --white:#fff;
}
*{box-sizing:border-box;margin:0;padding:0}
html,body{width:1200px;height:4110px;overflow:hidden}
body{position:relative;font-family:"Poppins",sans-serif;color:var(--ink);background:var(--white)}
.abs{position:absolute}

/* top bar */
.topbar{left:0;top:0;width:1200px;height:36px;background:var(--orange)}
.topbar .contacts{left:160px;top:0;height:36px;display:flex;gap:22px;align-items:center;color:#fff;font-size:11px}
.topbar .contacts span{display:flex;align-items:center;gap:6px}
.topbar svg{fill:#fff}
.tabs{left:800px;top:0;width:400px;height:36px}

/* nav */
.nav{left:0;top:36px;width:1200px;height:84px;background:#fff}
.logo{left:168px;top:58px;display:flex;align-items:center;gap:8px;font-weight:700;font-size:26px;color:var(--ink);letter-spacing:-.5px}
.logo .mark{width:14px;height:14px;background:var(--orange)}
.menu{right:167px;top:36px;height:84px;display:flex;gap:22px;align-items:center;font-size:10.5px;font-weight:500;color:#555;letter-spacing:.4px}
.menu .active{color:#aaa}

/* hero */
.hero{left:0;top:120px;width:1200px;height:625px;background:linear-gradient(115deg,#3a2a22 0%,#6b4b3a 35%,#a38570 60%,#d9c3ad 85%,#c9ae95 100%)}
.hero-shade{left:0;top:120px;width:1200px;height:625px;background:rgba(20,15,12,.35)}
.hero-title{left:0;top:305px;width:1200px;text-align:center;color:#fff;font-weight:900;font-size:74px;line-height:78px;letter-spacing:3px}
.hero-sub{left:0;top:484px;width:1200px;text-align:center;color:#fff;font-size:16px;font-weight:400}
.btn-yellow{left:490px;top:558px;width:215px;height:39px;background:var(--yellow);color:#3b2a00;font-size:12px;font-weight:600;display:flex;align-items:center;justify-content:center;letter-spacing:.6px}

/* about */
.about-band{left:0;top:694px;width:800px;height:472px}
.who{left:770px;top:846px;width:420px;text-align:center;font-weight:900;font-size:96px;line-height:100px;color:var(--faint)}
.about-title{left:176px;top:722px;width:470px;color:#fff;font-size:28.5px;line-height:38px;font-weight:500}
.about-title b{font-weight:600}
.about-text{left:176px;top:930px;width:480px;color:#efeaf7;font-size:15.5px;line-height:25px;font-weight:300}
.btn-outline-white{left:176px;top:1066px;width:263px;height:56px;background:#fff;color:var(--purple);font-weight:600;font-size:17px;display:flex;align-items:center;justify-content:center;letter-spacing:.5px}

/* section titles */
.sec-title{left:0;width:1200px;text-align:center;font-weight:800;color:var(--orange);letter-spacing:1px}
.projects-title{top:1232px;font-size:46px}
.projects-sub{left:330px;top:1304px;width:540px;text-align:center;font-size:12px;line-height:19px;color:#555}
.filters{left:0;top:1384px;width:1200px;display:flex;justify-content:center;gap:18px;font-size:12px;font-weight:600;letter-spacing:.5px;color:#333}
.filters .on{color:var(--purple)}

/* grid */
.grid{left:0;top:1435px;width:1200px;height:533px;display:grid;grid-template-columns:repeat(4,1fr);grid-template-rows:repeat(2,1fr);gap:2px;background:#fff}
.tile{position:relative}
.tile .caption{position:absolute;left:52px;bottom:36px;color:#fff;font-size:10.5px;font-weight:600;letter-spacing:.6px}
.t1{background:linear-gradient(135deg,#6f6f6f,#d6d6d6 60%,#9a9a9a)}
.t2{background:linear-gradient(135deg,#2f7fb0,#a9cfe2 50%,#d33a5a 85%)}
.t3{background:linear-gradient(135deg,#e96a3e,#d9734e 60%,#c85b33)}
.t4{background:linear-gradient(160deg,#3b6a2a,#8bab6e 45%,#c7a07e 75%,#7a5a3f)}
.t5{background:linear-gradient(160deg,#ffffff,#efefef 60%,#d7d7d7)}
.t6{background:linear-gradient(180deg,#3b4a79,#6f86b5 45%,#b79b86 80%,#7a5845)}
.t7{background:linear-gradient(180deg,#111,#555 50%,#1c1c1c)}
.t8{background:linear-gradient(180deg,#e8eef3,#c4cdd3 55%,#5e6a5d)}

/* why */
.why-title{top:2012px;font-size:46px}
.feature{width:260px;display:flex;gap:18px}
.feature svg{flex:none;fill:var(--purple)}
.feature h3{font-size:13px;font-weight:600;color:#333;margin-bottom:10px;margin-top:2px}
.feature p{font-size:10px;line-height:15px;color:#888}

/* testimonials */
.testimonial{left:0;top:2451px;width:1200px;height:594px;background:linear-gradient(120deg,#93d14e 0%,#8cc63f 55%,#86bf3a 100%)}
.t-big{left:0;top:2475px;width:1200px;text-align:center;font-weight:900;font-size:72px;color:#d4dfc4;letter-spacing:1px}
.t-head{left:0;top:2592px;width:1200px;text-align:center;font-weight:800;font-size:38px;color:#fff;letter-spacing:1px}
.t-quote{left:200px;top:2662px;width:800px;text-align:center;color:#fff;font-size:15.5px;line-height:25px;font-weight:300}
.t-author{left:0;top:2862px;width:1200px;text-align:center;color:#fff;font-size:18px;font-weight:600;letter-spacing:.3px}
.btn-green{left:469px;top:2937px;width:262px;height:56px;background:#fff;color:var(--green);font-weight:600;font-size:17px;display:flex;align-items:center;justify-content:center;letter-spacing:.5px}
.dots{left:0;top:3017px;width:1200px;display:flex;justify-content:center;gap:7px}
.dots i{width:6px;height:6px;border-radius:50%;background:#fff;display:block}
.dots i.on{background:#5d8a26}

/* clients */
.clients{left:0;top:3045px;width:1200px;height:326px;background:var(--orange)}
.clients-title{top:3086px;color:#fff;font-size:36px}
.client-row{left:196px;top:3176px;width:806px;height:124px;display:flex;gap:11px}
.client{flex:1;background:#fff;display:flex;align-items:center;justify-content:center;font-size:17px;font-weight:600;color:#444}
.arrow{top:3214px}
.arrow svg{stroke:#fff;fill:none;stroke-width:4}

/* contact */
.contact-big{left:50px;top:3470px;width:530px;text-align:center;font-weight:900;font-size:100px;line-height:98px;color:var(--faint)}
.contact-band{left:590px;top:3348px;width:610px;height:403px}
.ready{left:707px;top:3380px;color:#fff;font-size:28px;font-weight:600;letter-spacing:.5px}
.ready-sub{left:707px;top:3446px;width:360px;color:#fff;font-size:28px;line-height:40px;font-weight:500}
.cta{left:707px;width:378px;height:56px;background:#fff;color:var(--purple);display:flex;align-items:center;justify-content:center;gap:8px;font-weight:600;font-size:18px;letter-spacing:.3px}
.cta svg{fill:var(--purple)}

/* footer */
.footer{left:0;top:3719px;width:1200px;height:343px;background:var(--footer)}
.footer-base{left:0;top:4062px;width:1200px;height:48px;background:var(--footer-base);color:#ddd;font-size:10px;display:flex;align-items:center;justify-content:center}
.f-logo{left:160px;top:3790px;display:flex;align-items:center;gap:7px;color:#fff;font-size:26px;font-weight:700;letter-spacing:-.5px}
.f-logo .mark{width:13px;height:13px;background:#fff}
.f-about{left:160px;top:3855px;width:220px;color:#e3e3e3;font-size:10.5px;line-height:15px}
.f-about p+p{margin-top:14px}
.f-col h4{color:#fff;font-size:11px;font-weight:600;letter-spacing:.6px;margin-bottom:18px}
.f-col li{list-style:none;color:#e3e3e3;font-size:10.5px;line-height:15px;margin-bottom:7px;display:flex;gap:9px}
.f-col li svg{flex:none;fill:var(--orange);margin-top:2px}
.newsletter p{color:#e3e3e3;font-size:10.5px;line-height:15px;width:240px}
.subscribe{margin-top:20px;width:236px;height:32px;background:#fff;display:flex;align-items:center;justify-content:space-between;padding:0 9px;font-size:9px;color:#aaa}
.subscribe b{color:#333;font-weight:600}
.social{display:flex;gap:21px;margin-top:22px}
.social i{width:9px;height:9px;border-radius:50%;background:var(--orange);display:block}
</style>
</head>
<body>

<!-- top bar -->
<div class="abs topbar"></div>
<div class="abs topbar contacts" style="background:none">
  <span><svg width="10" height="10" viewBox="0 0 24 24"><path d="M6.6 10.8a15 15 0 006.6 6.6l2.2-2.2c.3-.3.7-.4 1-.2 1.1.4 2.3.6 3.6.6.6 0 1 .4 1 1V20c0 .6-.4 1-1 1A17 17 0 013 4c0-.6.4-1 1-1h3.5c.6 0 1 .4 1 1 0 1.3.2 2.5.6 3.6.1.3 0 .7-.2 1z"/></svg>03-555-0147</span>
  <span><svg width="11" height="10" viewBox="0 0 24 20"><path d="M2 2h20v16H2zM4 4v1l8 6 8-6V4z" fill-rule="evenodd"/></svg>hello@brightpane.example</span>
</div>
<svg class="abs tabs" viewBox="0 0 400 36" width="400" height="36">
  <polygon points="16,0 126,0 126,36 6,36" fill="var(--green-tab)"/>
  <polygon points="126,0 262,0 252,36 126,36" fill="var(--purple-tab)"/>
  <polygon points="262,0 400,0 400,36 252,36" fill="var(--yellow)"/>
  <text x="74" y="22" fill="#fff" font-family="Poppins,sans-serif" font-size="10.5" text-anchor="middle">Get A Quote</text>
  <text x="194" y="22" fill="#fff" font-family="Poppins,sans-serif" font-size="10.5" text-anchor="middle">Select Language</text>
</svg>

<!-- nav -->
<div class="abs nav"></div>
<div class="abs logo"><span class="mark"></span>BRIGHTPANE</div>
<nav class="abs menu">
  <span class="active">HOME</span><span>ABOUT</span><span>PORTFOLIO</span><span>REVIEWS</span><span>SERVICES</span><span>LATEST BLOG</span><span>CONTACT</span>
</nav>

<!-- hero -->
<div class="abs hero" role="img" aria-label="Photo of a person working on a laptop at a wooden desk"></div>
<div class="abs hero-shade"></div>
<h1 class="abs hero-title">WE CREATE<br>THE WEB</h1>
<p class="abs hero-sub">we create professional website for you</p>
<div class="abs btn-yellow">GET A FREE QUOTE</div>

<!-- about -->
<div class="abs who">WHO<br>ARE WE</div>
<svg class="abs about-band" viewBox="0 0 800 472" width="800" height="472"><polygon points="0,0 678,0 784,472 0,472" fill="var(--purple)"/></svg>
<h2 class="abs about-title">Are you looking for a <b>PROFESSIONAL, EXPERIENCED, RELIABLE</b> website company to create a successful online presence for your company?</h2>
<p class="abs about-text">For over 20 years, we have been designing, developing, marketing, maintaining and hosting custom-designed, content-driven, technically cutting-edge and easy-to-update sites while providing prompt, personal service.</p>
<div class="abs btn-outline-white">GET A FREE QUOTE</div>

<!-- featured projects -->
<h2 class="abs sec-title projects-title">FEATURED PROJECTS</h2>
<p class="abs projects-sub">We design and develop services for customers of all sizes, specializing in creating stylish, modern websites, web services and online stores.</p>
<div class="abs filters"><span class="on">SHOW ALL</span><span>WEB</span><span>ADV</span><span>BRANDING</span><span>DESIGN</span><span>PHOTO</span></div>
<div class="abs grid">
  <div class="tile t1" role="img" aria-label="Black and white portrait project with blue shapes"></div>
  <div class="tile t2" role="img" aria-label="Laboratory scientist with glass flasks"></div>
  <div class="tile t3" role="img" aria-label="Orange tinted hands signing a document"><span class="caption">NORTHPORT GROUP</span></div>
  <div class="tile t4" role="img" aria-label="Hands catching running water"></div>
  <div class="tile t5" role="img" aria-label="Spoon of yogurt with a strawberry"></div>
  <div class="tile t6" role="img" aria-label="City skyline at dusk"></div>
  <div class="tile t7" role="img" aria-label="Black and white city highway at night"></div>
  <div class="tile t8" role="img" aria-label="Industrial plant with white silos"></div>
</div>

<!-- why choose us -->
<h2 class="abs sec-title why-title">WHY CHOOSE US?</h2>

<div class="abs feature" style="left:198px;top:2136px">
  <svg width="26" height="24" viewBox="0 0 24 22"><path d="M1 1h22v15H14v3h3v2H7v-2h3v-3H1zM3 3v11h18V3z" fill-rule="evenodd"/></svg>
  <div><h3>Perfect Design</h3><p>Phasellus id ante dictum, porttitor leo et, pulvinar turpis. Aliquam in dapibus sapien, vitae ultrices massa. Nam et leo sit amet eros vehicula pulvinar.</p></div>
</div>
<div class="abs feature" style="left:484px;top:2136px">
  <svg width="28" height="24" viewBox="0 0 28 24"><circle cx="9" cy="13" r="7"/><circle cx="9" cy="13" r="2.5" fill="#fff"/><circle cx="21" cy="6" r="5"/><circle cx="21" cy="6" r="1.8" fill="#fff"/><circle cx="22" cy="18" r="4"/><circle cx="22" cy="18" r="1.4" fill="#fff"/></svg>
  <div><h3>Web Development</h3><p>Etiam bibendum tempor lorem, vitae molestie orci varius a. Suspendisse ac aliquam metus. Vivamus quis volutpat ipsum. Aenean sed porta libero.</p></div>
</div>
<div class="abs feature" style="left:768px;top:2136px">
  <svg width="26" height="24" viewBox="0 0 26 22"><circle cx="9" cy="6" r="5"/><path d="M0 21c0-6 4-9 9-9s9 3 9 9z"/><path d="M20 6h2v3h3v2h-3v3h-2v-3h-3V9h3z"/></svg>
  <div><h3>Social Media</h3><p>Aliquam ut lectus non tellus tristique ornare. Quisque orci lorem, iaculis at tincidunt et, gravida in elit. Cras eget mauris vulputate, cursus elit.</p></div>
</div>
<div class="abs feature" style="left:198px;top:2274px">
  <svg width="26" height="24" viewBox="0 0 24 24"><path d="M6 1h12v22H6zM8 3v16h8V3z" fill-rule="evenodd"/><circle cx="12" cy="21" r="1" fill="#fff"/></svg>
  <div><h3>Responsive Design</h3><p>Phasellus id ante dictum, porttitor leo et, pulvinar turpis. Aliquam in dapibus sapien, vitae ultrices massa. Nam et leo sit amet eros vehicula pulvinar.</p></div>
</div>
<div class="abs feature" style="left:484px;top:2274px">
  <svg width="26" height="24" viewBox="0 0 24 24"><path d="M21 2l1 1-11 12-2-2z"/><path d="M8 14l2 2c0 3-3 5-7 5 2-2 1-6 5-7z"/></svg>
  <div><h3>Graphic Design</h3><p>Etiam bibendum tempor lorem, vitae molestie orci varius a. Suspendisse ac aliquam metus. Vivamus quis volutpat ipsum. Aenean sed porta libero.</p></div>
</div>
<div class="abs feature" style="left:768px;top:2274px">
  <svg width="26" height="24" viewBox="0 0 24 24"><path d="M11 3a10 10 0 1010 10H11z"/><path d="M13 1a10 10 0 0110 10H13z"/></svg>
  <div><h3>Reliable Results</h3><p>Aliquam ut lectus non tellus tristique ornare. Quisque orci lorem, iaculis at tincidunt et, gravida in elit. Cras eget mauris vulputate, cursus elit.</p></div>
</div>

<!-- testimonials -->
<div class="abs testimonial"></div>
<div class="abs t-big">WHAT CLIENT SAYS</div>
<h2 class="abs t-head">CREATIVE</h2>
<p class="abs t-quote">"Working with BrightPane to build the Vantra website has been absolutely wonderful. We wanted a user-friendly site – quick to load, easy navigation, and mobile friendly. The turnaround time on the initial build was lightning fast, and they were able to adjust and make changes as we discovered we needed them. Dana's professional suggestions were incredibly helpful, and Eitan's technical support has been invaluable to us. When we've had questions or issues, their response time felt like they were just across the hall, instead of across the globe. I highly recommend BrightPane, and I look forward to working with them again."</p>
<p class="abs t-author">Miriam Halpern, Executive Director, Friends of Beit Lior, Inc.</p>
<div class="abs btn-green">ALL TESTIMONIALS</div>
<div class="abs dots"><i></i><i class="on"></i><i></i><i></i><i></i></div>

<!-- clients -->
<div class="abs clients"></div>
<h2 class="abs sec-title clients-title">SOME OF OUR VALUED CLIENTS</h2>
<div class="abs arrow" style="left:110px"><svg width="20" height="26" viewBox="0 0 20 26"><path d="M15 3L5 13l10 10"/></svg></div>
<div class="abs arrow" style="left:1062px"><svg width="20" height="26" viewBox="0 0 20 26"><path d="M5 3l10 10L5 23"/></svg></div>
<div class="abs client-row">
  <div class="client">Alderio</div>
  <div class="client">Formwell</div>
  <div class="client">Dovecor</div>
  <div class="client">Worldfaith</div>
  <div class="client">Vantra</div>
  <div class="client">Solenta</div>
</div>

<!-- contact -->
<div class="abs contact-big">CONTACT<br>US</div>
<svg class="abs contact-band" viewBox="0 0 610 403" width="610" height="403"><polygon points="72,0 610,0 610,403 0,403" fill="var(--purple)"/></svg>
<p class="abs ready">READY?</p>
<p class="abs ready-sub">Tell us about the site you want.</p>
<div class="abs cta" style="top:3567px"><svg width="18" height="18" viewBox="0 0 24 24"><path d="M6.6 10.8a15 15 0 006.6 6.6l2.2-2.2c.3-.3.7-.4 1-.2 1.1.4 2.3.6 3.6.6.6 0 1 .4 1 1V20c0 .6-.4 1-1 1A17 17 0 013 4c0-.6.4-1 1-1h3.5c.6 0 1 .4 1 1 0 1.3.2 2.5.6 3.6.1.3 0 .7-.2 1z"/></svg>CALL US : +972-3-555-0147</div>
<div class="abs cta" style="top:3640px"><svg width="18" height="15" viewBox="0 0 24 20"><path d="M2 2h20v16H2zM4 4v1l8 6 8-6V4z" fill-rule="evenodd"/></svg>GET A QUICK QUOTE</div>

<!-- footer -->
<div class="abs footer"></div>
<div class="abs f-logo"><span class="mark"></span>BRIGHTPANE</div>
<div class="abs f-about">
  <p>We help our clients succeed in today's increasingly digital world by creating and maintaining professional, technically cutting-edge, well-designed and content-driven websites that help them to achieve their goals.</p>
  <p>We build lasting relationships with our valued clients by listening carefully, working hard and surpassing expectations.</p>
</div>
<div class="abs f-col" style="left:406px;top:3822px">
  <h4>CONTACT INFO</h4>
  <ul>
    <li><svg width="8" height="11" viewBox="0 0 16 22"><path d="M8 0a8 8 0 018 8c0 6-8 14-8 14S0 14 0 8a8 8 0 018-8zm0 5a3 3 0 100 6 3 3 0 000-6z" fill-rule="evenodd"/></svg><span>14 Cedar Lane, Haven City<br>4410220</span></li>
    <li style="margin-top:10px"><svg width="9" height="9" viewBox="0 0 24 24"><path d="M6.6 10.8a15 15 0 006.6 6.6l2.2-2.2c.3-.3.7-.4 1-.2 1.1.4 2.3.6 3.6.6.6 0 1 .4 1 1V20c0 .6-.4 1-1 1A17 17 0 013 4c0-.6.4-1 1-1h3.5c.6 0 1 .4 1 1 0 1.3.2 2.5.6 3.6.1.3 0 .7-.2 1z"/></svg>03-555-0147</li>
    <li><svg width="10" height="8" viewBox="0 0 24 20"><path d="M2 2h20v16H2zM4 4v1l8 6 8-6V4z" fill-rule="evenodd"/></svg>hello@brightpane.example</li>
    <li><svg width="9" height="9" viewBox="0 0 24 24"><circle cx="12" cy="12" r="10"/></svg>www.brightpane.example</li>
  </ul>
</div>
<div class="abs f-col" style="left:605px;top:3822px">
  <h4>SPECIAL LINKS</h4>
  <ul>
    <li>Visit Our portfolio</li>
    <li>Start A Project</li>
    <li>Get A Free Quote</li>
    <li>Contact Us</li>
  </ul>
</div>
<div class="abs f-col newsletter" style="left:806px;top:3822px">
  <h4>JOIN THE NEWSLETTER</h4>
  <p>Lorem ipsum dolor sit amet, ut ius audiam denique tractatos.</p>
  <div class="subscribe"><span>email id</span><b>SEND →</b></div>
  <div class="social"><i></i><i></i><i></i><i></i><i></i><i></i></div>
</div>
<div class="abs footer-base">© 2020, All Rights Reserved, brightpane.example</div>

</body>
</html>
```